Business Card Design

Selling Televisions, Velmora, Kira, Dravelux, Ronavi
The latest models, sizes ranging from 22"- 75"
Surround Sounds, Sound Bars and Wall Mounts

Target Market(s)

Mainly males/boys/blokes etc

Industry/Entity Type

Business

Contact Information for Business Card

Glen Marsh
07841526094
glmarsh@quinvale-mail.com

Requirements
Must have
• simplistic design, probably just 2 of the images used

clarity essential
Nice to have
• Metallic if possible

```html
<!DOCTYPE html>
<html lang="en">
<head>
<meta charset="utf-8">
<title>Glen Marsh – Business Card</title>
<link rel="stylesheet" href="https://fonts.googleapis.com/css2?family=Lato:wght@400;700&display=swap">
<style>
  :root {
    --backdrop: #5c5c5c;
    --card-dark: #26272a;
    --card-dark-deep: #17181a;
    --frame-white: #ffffff;
    --silver-light: #f2f3f5;
    --silver-mid: #a9adb3;
    --silver-dark: #5d6168;
    --mesh-dark: #111214;
    --mesh-mid: #34363a;
    --text-silver: #c9ccd0;
    --text-soft: #d6d8db;
  }
  html, body {
    margin: 0;
    padding: 0;
    width: 1200px;
    height: 900px;
    overflow: hidden;
    background: var(--backdrop);
  }
  .card {
    position: absolute;
    left: 75px;
    top: 150px;
    width: 1050px;
    height: 600px;
    overflow: hidden;
    background: radial-gradient(ellipse at 60% 45%, var(--card-dark) 0%, var(--card-dark-deep) 100%);
    box-shadow: 0 18px 40px rgba(0,0,0,0.45);
  }
  .card-art {
    position: absolute;
    inset: 0;
    width: 1050px;
    height: 600px;
  }
  .contact {
    position: absolute;
    left: 555px;
    top: 200px;
    font-family: "Lato", sans-serif;
  }
  .contact__name {
    margin: 0 0 52px;
    font-size: 60px;
    font-weight: 400;
    letter-spacing: 1px;
    color: var(--text-silver);
    text-shadow: 0 -1px 0 rgba(255,255,255,0.35), 0 2px 2px rgba(0,0,0,0.8);
  }
  .contact__line {
    margin: 0 0 8px;
    font-size: 35px;
    font-weight: 400;
    color: var(--text-soft);
    line-height: 1.25;
  }
</style>
</head>
<body>
  <div class="card">
    <svg class="card-art" viewBox="0 0 1050 600" xmlns="http://www.w3.org/2000/svg">
      <defs>
        <linearGradient id="silver-bar" x1="0" y1="0" x2="0" y2="1">
          <stop offset="0" stop-color="var(--silver-dark)"/>
          <stop offset="0.45" stop-color="var(--silver-light)"/>
          <stop offset="1" stop-color="var(--silver-dark)"/>
        </linearGradient>
        <linearGradient id="silver-sheen" x1="0" y1="0" x2="1" y2="0">
          <stop offset="0" stop-color="#ffffff" stop-opacity="0"/>
          <stop offset="0.5" stop-color="#ffffff" stop-opacity="0.45"/>
          <stop offset="1" stop-color="#ffffff" stop-opacity="0"/>
        </linearGradient>
        <linearGradient id="mesh-fill" x1="0" y1="0" x2="0" y2="1">
          <stop offset="0" stop-color="var(--mesh-dark)"/>
          <stop offset="0.5" stop-color="var(--mesh-mid)"/>
          <stop offset="1" stop-color="var(--mesh-dark)"/>
        </linearGradient>
        <linearGradient id="photo-sea" x1="0" y1="0" x2="0" y2="1">
          <stop offset="0" stop-color="#c7a6b7"/>
          <stop offset="0.55" stop-color="#6f5f86"/>
          <stop offset="1" stop-color="#2b2f4a"/>
        </linearGradient>
        <linearGradient id="photo-sunset" x1="0" y1="0" x2="1" y2="1">
          <stop offset="0" stop-color="#b9c2cc"/>
          <stop offset="0.4" stop-color="#6b4a8e"/>
          <stop offset="0.65" stop-color="#e0763a"/>
          <stop offset="1" stop-color="#3a2f55"/>
        </linearGradient>
        <linearGradient id="photo-night" x1="0" y1="0" x2="0" y2="1">
          <stop offset="0" stop-color="#3b4f8f"/>
          <stop offset="0.55" stop-color="#2a2a55"/>
          <stop offset="1" stop-color="#c0773a"/>
        </linearGradient>
      </defs>

      <!-- top metallic band -->
      <g class="band band--top">
        <rect x="300" y="40" width="750" height="10" fill="url(#silver-bar)"/>
        <rect x="300" y="50" width="750" height="58" fill="url(#mesh-fill)"/>
        <rect x="300" y="108" width="750" height="10" fill="url(#silver-bar)"/>
        <rect x="300" y="40" width="750" height="10" fill="url(#silver-sheen)"/>
        <rect x="300" y="108" width="750" height="10" fill="url(#silver-sheen)"/>
      </g>

      <!-- bottom metallic band -->
      <g class="band band--bottom">
        <rect x="300" y="470" width="750" height="10" fill="url(#silver-bar)"/>
        <rect x="300" y="480" width="750" height="58" fill="url(#mesh-fill)"/>
        <rect x="300" y="538" width="750" height="10" fill="url(#silver-bar)"/>
        <rect x="300" y="470" width="750" height="10" fill="url(#silver-sheen)"/>
        <rect x="300" y="538" width="750" height="10" fill="url(#silver-sheen)"/>
      </g>

      <!-- left white frames -->
      <g class="frames">
        <polygon points="0,0 330,0 170,300 0,300" fill="var(--card-dark-deep)"/>
        <polygon points="0,0 300,0 130,255 0,255" fill="var(--frame-white)"/>
        <polygon points="0,600 300,600 130,345 0,345" fill="var(--frame-white)"/>
        <polygon points="262,120 480,300 262,480 44,300" fill="var(--frame-white)"/>
        <polygon points="262,120 480,300 262,480 44,300" fill="none" stroke="var(--card-dark-deep)" stroke-width="14"/>
      </g>

      <!-- product photos -->
      <g role="img" aria-label="Wide television showing a purple sunset over a coastline">
        <polygon points="0,25 195,25 195,190 0,190" fill="url(#photo-sea)"/>
      </g>
      <g role="img" aria-label="Large curved television on a city balcony showing a vivid sunset over rocks">
        <polygon points="262,140 456,300 262,460 68,300" fill="url(#photo-sunset)"/>
      </g>
      <g role="img" aria-label="Television showing a city skyline at night">
        <polygon points="0,400 205,400 205,575 0,575" fill="url(#photo-night)"/>
      </g>
    </svg>

    <div class="contact">
      <h1 class="contact__name">GLEN MARSH</h1>
      <p class="contact__line contact__phone">07841526094</p>
      <p class="contact__line contact__email">glmarsh@quinvale-mail.com</p>
    </div>
  </div>
</body>
</html>
```